Sticker olive oil

Good day,
I would like to design a sticker that will be stuck on an olive oil bottle. It should have the manufacturer's picture on it (in the background, as a hologram, ....?). The brand is a made-up word, composed of the name of the producer "Bertoldo" and the Italian "Olio" for oil. So composed: BertoldOlio; the double "O" in the middle could be represented as an olive, then there is an immediate reference to the olive oil. Other textual content should be:
Main brand: "BertoldOlio"
Description: "cold pressed, pure olive oil from the Valle - Morsa (Castrucco)
Addition: "guaranteed untreated"
You can reach me via my email info@kremvato.de
Payment via PayPal; budget 50 €
I'm still trying to upload the current label, the picture of Bertoldo too

BertoldOlio

```html
<!DOCTYPE html>
<html lang="en">
<head>
<meta charset="utf-8">
<title>BertoldOlio – Olive Oil Label</title>
<link rel="stylesheet" href="https://fonts.googleapis.com/css2?family=Gelasio:wght@400;500&display=swap">
<style>
  :root {
    --backdrop: #f4eadc;
    --label-olive: #2a2e05;
    --cream: #f7f6c8;
    --leaf-green: #a5c23a;
    --brand-green: #b8cc5a;
    --photo-light: #f6f3cf;
    --photo-navy: #27345a;
  }
  * { margin: 0; padding: 0; box-sizing: border-box; }
  html, body {
    width: 1080px;
    height: 1200px;
    overflow: hidden;
    background: var(--backdrop);
  }
  .canvas {
    position: relative;
    width: 1080px;
    height: 1200px;
  }
  .label {
    position: absolute;
    left: 100px;
    top: 73px;
    width: 880px;
    height: 1054px;
    display: block;
  }
  .label-ground { fill: var(--label-olive); }
  .frame-outer, .frame-inner { fill: none; stroke: var(--cream); }
  .frame-outer { stroke-width: 6; }
  .frame-inner { stroke-width: 2.5; }
  .frame-middle { fill: none; stroke: var(--leaf-green); stroke-width: 5; }
  .medallion-ring { fill: var(--label-olive); stroke: var(--cream); stroke-width: 6; }
  .medallion-band { fill: none; stroke: var(--leaf-green); stroke-width: 4; }
  .text-serif { font-family: "Gelasio", Georgia, serif; }
  .brand-name { fill: var(--brand-green); font-size: 106px; font-weight: 400; }
  .brand-dot { fill: var(--brand-green); }
  .subtitle { fill: var(--cream); font-size: 46px; font-weight: 500; letter-spacing: 1px; }
  .product-name { fill: var(--cream); font-size: 63px; font-weight: 500; letter-spacing: 1.5px; }
  .origin-line { fill: var(--leaf-green); font-size: 30px; letter-spacing: 1.5px; }
  .volume { fill: var(--cream); font-size: 36px; letter-spacing: 1.5px; }
</style>
</head>
<body>
<main class="canvas">
  <svg class="label" viewBox="0 0 785 940" xmlns="http://www.w3.org/2000/svg">
    <defs>
      <linearGradient id="rule-fade" x1="0" x2="1" y1="0" y2="0">
        <stop offset="0" stop-color="#a5c23a" stop-opacity="0"/>
        <stop offset="0.5" stop-color="#a5c23a" stop-opacity="1"/>
        <stop offset="1" stop-color="#a5c23a" stop-opacity="0"/>
      </linearGradient>
      <radialGradient id="portrait-tone" cx="0.5" cy="0.35" r="0.7">
        <stop offset="0" stop-color="#f6f3cf"/>
        <stop offset="0.45" stop-color="#c9b9a4"/>
        <stop offset="1" stop-color="#27345a"/>
      </radialGradient>
    </defs>

    <rect class="label-ground" x="0" y="0" width="785" height="940"/>

    <!-- stepped frame (top middle hidden behind the medallion) -->
    <path class="frame-outer" d="M383 100 L476 110 Q570 140 665 164 V212 H737 V859 H680 V905 H105 V859 H45 V212 H105 V164 Q200 140 290 110 Z"/>
    <path class="frame-middle" d="M383 114 L471 124 Q560 152 652 175 V225 H724 V846 H667 V892 H118 V846 H58 V225 H118 V175 Q205 152 295 124 Z"/>
    <path class="frame-inner" d="M383 126 L466 136 Q555 162 642 184 V235 H714 V836 H657 V882 H128 V836 H68 V235 H128 V184 Q210 162 300 136 Z"/>

    <!-- portrait medallion -->
    <ellipse class="medallion-ring" cx="383" cy="149" rx="116" ry="130"/>
    <ellipse class="medallion-band" cx="383" cy="149" rx="104" ry="118"/>
    <ellipse cx="383" cy="149" rx="95" ry="108" fill="url(#portrait-tone)" role="img" aria-label="Portrait photograph of the olive oil producer, Bertoldo"/>

    <!-- brand name -->
    <text class="text-serif brand-name" x="380" y="489" text-anchor="middle">BertoldOlio</text>
    <circle class="brand-dot" cx="662" cy="455" r="10"/>

    <rect x="115" y="517" width="555" height="3" fill="url(#rule-fade)"/>

    <text class="text-serif subtitle" x="388" y="577" text-anchor="middle">COLD PRESSED</text>
    <text class="text-serif product-name" x="393" y="642" text-anchor="middle">PURE OLIVE OIL</text>

    <rect x="115" y="668" width="555" height="3" fill="url(#rule-fade)"/>

    <text class="text-serif origin-line" x="391" y="722" text-anchor="middle">THE VALLE MORSA-CASTRUCCO</text>
    <text class="text-serif origin-line" x="391" y="767" text-anchor="middle">GUARANTEED UNTREATED</text>

    <text class="text-serif volume" x="392" y="865" text-anchor="middle">750 ml</text>
  </svg>
</main>
</body>
</html>
```